METAL FABRICATION BUSINESS CARD

** I will be ending the project and picking design early. This Friday October 3rd at 7am MST if not sooner**
ONE SIDED BUSINESS CARD ONLY. AND LOGO SIZE TO BE DOMINANT so it stands out.
Looking for a black background and will be doing raised chrome/silver font on the business cards. Looking to have the following on the front of the business card. Company logo is uploaded in files.
Company logo
*Compartment Doors
*Roof Radius Metal
*J-Wrap Metal Skirting
*S-Lock Beltline Molding
*Pre-Bent Molding
and more...
Owen Baskell 406.529.1847 info@Trelvo-Works.com
Updates
One sided business card only please. Also logo size should be dominant and sized bigger
Contact Information for Business Card
Black background, Text will be raised chrome/silver, and corners will be rounded.

```html
<!DOCTYPE html>
<html lang="en">
<head>
<meta charset="utf-8">
<title>Trelvo-Works Business Card</title>
<link rel="stylesheet" href="https://fonts.googleapis.com/css2?family=Montserrat:wght@800&family=Poppins:wght@300;400;600&display=swap">
<style>
  :root {
    --backdrop: #222223;
    --card-top: #1f2024;
    --card-mid: #18191c;
    --card-low: #1c1d21;
    --silver: #d4d6da;
    --silver-dim: #9a9da3;
    --silver-light: #f1f2f4;
    --shadow: rgba(0,0,0,0.55);
  }
  * { margin: 0; padding: 0; box-sizing: border-box; }
  html, body { width: 1200px; height: 800px; overflow: hidden; background: var(--backdrop); }
  .canvas { position: relative; width: 1200px; height: 800px; display: flex; align-items: center; justify-content: center; }
  .card {
    position: relative; width: 420px; height: 720px; border-radius: 34px;
    background: var(--card-low); overflow: hidden;
    box-shadow: 0 18px 40px var(--shadow);
    font-family: "Poppins", sans-serif; color: var(--silver);
  }
  .card-layers { position: absolute; inset: 0; width: 100%; height: 100%; }
  .brand {
    position: absolute; top: 92px; left: 0; right: 0;
    display: flex; align-items: center; justify-content: center; gap: 12px;
  }
  .brand-dot { width: 26px; height: 26px; border-radius: 50%; background: var(--silver); }
  .brand-name { font-family: "Poppins", sans-serif; font-weight: 600; font-size: 40px; color: var(--silver); letter-spacing: 0.5px; }
  .contact { position: absolute; top: 268px; left: 0; right: 0; text-align: center; }
  .person-name {
    font-family: "Montserrat", sans-serif; font-weight: 800; font-size: 38px; letter-spacing: 0.5px;
    background: linear-gradient(180deg, var(--silver-light) 0%, #a9acb2 55%, #e6e7ea 100%);
    -webkit-background-clip: text; background-clip: text; color: transparent;
  }
  .contact-icons { display: flex; justify-content: center; gap: 10px; margin: 12px 0 10px; }
  .contact-icon {
    width: 32px; height: 32px; border-radius: 50%;
    background: radial-gradient(circle at 35% 30%, #eeeff1, #8d9096);
    display: flex; align-items: center; justify-content: center;
  }
  .contact-icon svg { width: 16px; height: 16px; }
  .contact-line { font-weight: 400; font-size: 19px; line-height: 30px; color: var(--silver); letter-spacing: 0.6px; }
  .services { position: absolute; top: 545px; left: 0; right: 0; text-align: center; list-style: none; }
  .services li { font-weight: 300; font-size: 17px; line-height: 25px; color: var(--silver); letter-spacing: 0.6px; }
  .services .more { color: var(--silver-dim); }
</style>
</head>
<body>
<div class="canvas">
  <div class="card">
    <svg class="card-layers" viewBox="0 0 420 720" preserveAspectRatio="none" aria-hidden="true">
      <defs>
        <linearGradient id="lowerFade" x1="0" y1="0" x2="0" y2="1">
          <stop offset="0" stop-color="#141518"/>
          <stop offset="1" stop-color="#1d1e22"/>
        </linearGradient>
      </defs>
      <rect width="420" height="720" fill="url(#lowerFade)"/>
      <path d="M0 0 H420 V520 C330 560 120 570 0 540 Z" fill="#1a1b1f"/>
      <path d="M0 0 H420 V450 C360 520 180 545 0 520 Z" fill="var(--card-top)"/>
      <path d="M0 520 C180 545 360 520 420 450" fill="none" stroke="#2a2b30" stroke-width="1"/>
    </svg>

    <div class="brand">
      <span class="brand-dot"></span>
      <span class="brand-name">Trelvo-Works</span>
    </div>

    <div class="contact">
      <div class="person-name">Owen Baskell</div>
      <div class="contact-icons">
        <span class="contact-icon">
          <svg viewBox="0 0 24 24"><path d="M6.6 10.8a15 15 0 0 0 6.6 6.6l2.2-2.2c.3-.3.7-.4 1-.2 1.1.4 2.3.6 3.6.6.6 0 1 .4 1 1V20c0 .6-.4 1-1 1A17 17 0 0 1 3 4c0-.6.4-1 1-1h3.5c.6 0 1 .4 1 1 0 1.3.2 2.5.6 3.6.1.3 0 .7-.2 1z" fill="#2a2b2f"/></svg>
        </span>
        <span class="contact-icon">
          <svg viewBox="0 0 24 24"><rect x="3" y="6" width="18" height="12" rx="1.5" fill="none" stroke="#2a2b2f" stroke-width="2"/><path d="M3.5 7l8.5 6 8.5-6" fill="none" stroke="#2a2b2f" stroke-width="2"/></svg>
        </span>
        <span class="contact-icon">
          <svg viewBox="0 0 24 24"><circle cx="12" cy="12" r="9" fill="none" stroke="#2a2b2f" stroke-width="2"/><ellipse cx="12" cy="12" rx="4" ry="9" fill="none" stroke="#2a2b2f" stroke-width="1.6"/><path d="M3 12h18" stroke="#2a2b2f" stroke-width="1.6"/></svg>
        </span>
      </div>
      <div class="contact-line">406.529.1847</div>
      <div class="contact-line">info@Trelvo-Works.com</div>
      <div class="contact-line">www.Trelvo-Works.com</div>
    </div>

    <ul class="services">
      <li>Compartment Doors</li>
      <li>Roof Radius Metal</li>
      <li>J-Wrap Metal Skirting</li>
      <li>S-Lock Beltline Molding</li>
      <li>Pre-Bent Molding</li>
      <li class="more">and more...</li>
    </ul>
  </div>
</div>
</body>
</html>
```